Church Grand Opening Bill Board design

I would like to create a bill board design for our church's grand opening. I would like to incorporate pictures of two separate preachers with a creative way of blending them both together so it won't take up too much space. I have included pictures and logo.

I am open for color coordination and I have included a couple of past designs to use as a reference

The information I would want on the Build Board is the following (1) Grand Opening (2) 4827 E. Pellford Street (3) 10:30am (4) Multi-Ethnic Church Planting Church (5) Sept. 26, 2021

Target Market(s)

Church shoppers and those who have never been connected to a church

Font styles to use
Serif

Requirements
Must have
• Our Logo
Nice to have
• i do not want any crosses or religious symbols

```html
<!DOCTYPE html>
<html lang="en">
<head>
<meta charset="utf-8">
<title>Kindle Church – Grand Opening Billboard</title>
<link href="https://fonts.googleapis.com/css2?family=Montserrat:wght@600;800;900&display=swap" rel="stylesheet">
<style>
  :root {
    --ink: #1c1c1c;
    --white: #ffffff;
    --orange-deep: #e8502e;
    --orange-mid: #ec6a2a;
    --orange-light: #f3991c;
    --ember: #f2a21e;
    --stage-bg: #dcdcdc;
  }
  * { margin: 0; padding: 0; box-sizing: border-box; }
  html, body { width: 978px; height: 1200px; overflow: hidden; background: var(--stage-bg); }
  body { font-family: "Montserrat", sans-serif; position: relative; }

  .billboard-frame {
    position: absolute; left: 39px; top: 394px;
    width: 900px; height: 413px; overflow: hidden;
  }
  .billboard {
    position: absolute; left: 0; top: 0;
    width: 1460px; height: 670px;
    transform: scale(0.6164); transform-origin: 0 0;
    background: var(--ink); overflow: hidden;
  }
  .billboard-shapes { position: absolute; inset: 0; width: 1460px; height: 670px; }

  .preacher-photo { position: absolute; }
  .preacher-photo--left {
    left: 27px; top: 52px; width: 340px; height: 618px;
    background: linear-gradient(180deg, #5a3d2e 0%, #2a2a2a 30%, #222 78%, #6f86a6 100%);
    clip-path: polygon(125px 0, 245px 0, 245px 118px, 340px 118px, 340px 618px, 10px 618px, 0 118px, 125px 118px);
  }
  .preacher-photo--right {
    left: 1098px; top: 28px; width: 345px; height: 642px;
    background: linear-gradient(180deg, #6b4a3a 0%, #2b2b2b 28%, #5d6470 60%, #2a2a2a 100%);
    clip-path: polygon(149px 0, 274px 0, 274px 142px, 345px 142px, 345px 642px, 70px 642px, 0 480px, 0 142px, 149px 142px);
  }

  .church-name {
    position: absolute; left: 300px; top: 116px;
    display: flex; align-items: center; gap: 12px;
    color: var(--white); font-weight: 800; font-size: 40px; line-height: 1;
    letter-spacing: -0.5px; white-space: nowrap;
  }
  .church-name__dot { width: 22px; height: 22px; border-radius: 50%; background: var(--ember); flex: none; }

  .divider { position: absolute; left: 677px; top: 72px; width: 3px; height: 158px; background: var(--white); }

  .event-details { position: absolute; left: 717px; top: 78px; list-style: none; }
  .event-details li { display: flex; align-items: center; gap: 31px; color: var(--white); font-weight: 800; white-space: nowrap; }
  .event-details svg { width: 26px; height: 26px; flex: none; }
  .event-details .detail-address { font-size: 32px; height: 44px; }
  .event-details .detail-date { font-size: 39px; height: 62px; }
  .event-details .detail-time { font-size: 39px; height: 56px; }

  .headline {
    position: absolute; left: 435px; top: 316px; width: 600px;
    color: var(--white); font-weight: 900; text-align: center;
  }
  .headline__line { display: block; white-space: nowrap; }
  .headline__line--grand { font-size: 150px; line-height: 150px; letter-spacing: -2px; }
  .headline__line--opening { font-size: 122px; line-height: 124px; letter-spacing: -1px; margin-top: 6px; }

  .tagline {
    position: absolute; left: 374px; top: 606px;
    color: var(--ink); font-weight: 900; font-size: 32px; letter-spacing: 0.3px;
    white-space: nowrap;
  }
</style>
</head>
<body>
  <div class="billboard-frame">
    <section class="billboard">
      <svg class="billboard-shapes" viewBox="0 0 1460 670" aria-hidden="true">
        <defs>
          <linearGradient id="bandGradient" x1="0" y1="0" x2="0.25" y2="1">
            <stop offset="0" stop-color="var(--orange-deep)"/>
            <stop offset="0.45" stop-color="var(--orange-mid)"/>
            <stop offset="1" stop-color="var(--orange-light)"/>
          </linearGradient>
        </defs>
        <path d="M0,670 L0,475 C120,405 260,330 420,322 C720,305 1040,230 1460,118 L1460,560 C1420,600 1390,632 1355,670 Z" fill="url(#bandGradient)"/>
        <path d="M340,292 C720,290 1100,200 1460,85" fill="none" stroke="#fff" stroke-width="3"/>
        <path d="M0,442 C20,428 40,416 60,404" fill="none" stroke="#fff" stroke-width="3"/>
        <path d="M1460,535 C1432,560 1412,578 1395,592" fill="none" stroke="#fff" stroke-width="3"/>
      </svg>

      <div class="preacher-photo preacher-photo--left" role="img" aria-label="Photo of the first preacher smiling, in a black polo shirt and jeans"></div>

      <div class="church-name"><span class="church-name__dot"></span>Kindle Church</div>
      <div class="divider"></div>

      <ul class="event-details">
        <li class="detail-address">
          <svg viewBox="0 0 24 24"><path d="M12 2a7 7 0 0 0-7 7c0 5 7 13 7 13s7-8 7-13a7 7 0 0 0-7-7zm0 9.5A2.5 2.5 0 1 1 12 6.5a2.5 2.5 0 0 1 0 5z" fill="#fff"/></svg>
          4827 E. Pellford Street
        </li>
        <li class="detail-date">
          <svg viewBox="0 0 24 24"><rect x="3" y="5" width="18" height="16" rx="2" fill="none" stroke="#fff" stroke-width="2"/><path d="M3 9h18M8 3v4M16 3v4" stroke="#fff" stroke-width="2"/><path d="M7 12h2v2H7zm4 0h2v2h-2zm4 0h2v2h-2zM7 16h2v2H7zm4 0h2v2h-2zm4 0h2v2h-2z" fill="#fff"/></svg>
          Sept. 26, 2021
        </li>
        <li class="detail-time">
          <svg viewBox="0 0 24 24"><path d="M5 2h14v2h-1.5c0 4-3 6-4.5 8 1.5 2 4.5 4 4.5 8H19v2H5v-2h1.5c0-4 3-6 4.5-8C9.5 10 6.5 8 6.5 4H5z" fill="#fff"/></svg>
          10:30am
        </li>
      </ul>

      <h1 class="headline">
        <span class="headline__line headline__line--grand">GRAND</span>
        <span class="headline__line headline__line--opening">OPENING</span>
      </h1>
      <p class="tagline">MULTI-ETHNIC CHURCH PLANTING CHURCH</p>

      <div class="preacher-photo preacher-photo--right" role="img" aria-label="Photo of the second preacher speaking with a headset mic, in a dark jacket over a grey shirt"></div>
    </section>
  </div>
</body>
</html>
```